Covid 19 Exit Strategy one page brochure

I would like to design, and will need URGENT help, a brochure detailing a Covid 19 Exit Strategy plan. This brochure will need to be understood easily and the graphics inside should make it easy for people to understand without reading the entire text. This project is quite urgent and needs to be completed THIS WEEK - by Saturday may 16th at the latest. I am attaching two examples. I will provide the text.

```html
<!DOCTYPE html>
<html lang="en">
<head>
<meta charset="utf-8">
<title>Coronavirus Covid-19 — Information And Guidelines</title>
<link rel="stylesheet" href="https://fonts.googleapis.com/css2?family=Montserrat:wght@400;500;600;700;800&family=Poppins:wght@400;500&display=swap">
<style>
  :root {
    --page-bg: #d9dde2;
    --blue-deep: #1c63c2;
    --blue-mid: #3a8de2;
    --blue-light: #8cc3f4;
    --blue-blob: #2f7fd8;
    --navy: #1f4690;
    --white: #ffffff;
    --text-soft: #eaf4ff;
    --photo-a: #eef2f6;
    --photo-b: #c6d7e7;
  }
  * { box-sizing: border-box; margin: 0; padding: 0; }
  html, body { width: 1200px; height: 938px; overflow: hidden; }
  body {
    background: var(--page-bg);
    font-family: "Montserrat", sans-serif;
    display: flex; align-items: center; justify-content: center;
  }
  .flyer {
    position: relative;
    width: 636px; height: 900px;
    overflow: hidden;
    background: linear-gradient(160deg, var(--blue-mid) 0%, var(--blue-light) 45%, var(--blue-mid) 80%, var(--blue-deep) 100%);
    box-shadow: 0 6px 24px rgba(0,0,0,.18);
  }
  .flyer-shapes { position: absolute; inset: 0; }
  .brand {
    position: absolute; left: 0; top: 0;
    width: 96px; height: 96px;
    background: var(--white);
    border-bottom-right-radius: 48px;
    display: flex; flex-direction: column; align-items: center; justify-content: center; gap: 6px;
  }
  .brand-mark { width: 24px; height: 24px; border: 2px solid var(--navy); border-radius: 50%; }
  .brand-name { font-size: 11px; font-weight: 600; color: var(--navy); letter-spacing: .5px; }
  .header { position: absolute; left: 0; right: 0; top: 118px; text-align: center; }
  .title { font-size: 43px; font-weight: 800; color: var(--navy); letter-spacing: -.5px; line-height: 1.1; }
  .subtitle { font-size: 33px; font-weight: 700; color: var(--white); line-height: 1.15; }
  .rule { width: 360px; height: 2px; background: var(--navy); margin: 10px auto 12px; }
  .kicker { font-size: 16px; font-weight: 800; color: var(--navy); letter-spacing: 1px; }
  .quote { font-family: "Poppins", sans-serif; font-size: 11px; color: var(--text-soft); width: 420px; margin: 8px auto 0; line-height: 1.45; }
  .guidelines { position: absolute; left: 56px; right: 36px; top: 372px; display: grid; grid-template-columns: 1fr 1fr; column-gap: 26px; }
  .column { display: flex; flex-direction: column; gap: 30px; }
  .column.right { margin-top: -60px; }
  .guide { display: flex; gap: 12px; align-items: flex-start; }
  .guide-icon { flex: 0 0 44px; height: 44px; margin-top: 18px; border-radius: 50%; background: var(--white); display: flex; align-items: center; justify-content: center; }
  .guide-heading { font-size: 16px; font-weight: 600; color: var(--white); margin-bottom: 3px; }
  .guide-text { font-family: "Poppins", sans-serif; font-size: 10.5px; line-height: 1.4; color: var(--text-soft); }
  .photo {
    position: absolute; right: 0; bottom: 0;
    width: 288px; height: 240px;
    border-top-left-radius: 120px;
    background: linear-gradient(135deg, var(--photo-a), var(--photo-b));
  }
  .contact { position: absolute; left: 40px; bottom: 38px; color: var(--white); }
  .contact-label { font-size: 19px; font-weight: 500; margin-bottom: 10px; }
  .contact-line { display: flex; align-items: center; gap: 8px; font-size: 16px; margin-bottom: 8px; }
  .social { display: flex; align-items: center; gap: 8px; font-size: 13px; font-weight: 500; margin-top: 8px; }
  .social-dot { width: 16px; height: 16px; border-radius: 50%; background: var(--white); }
</style>
</head>
<body>
<main class="flyer">
  <svg class="flyer-shapes" viewBox="0 0 636 900" aria-hidden="true">
    <path d="M0 0 H300 C330 40 300 90 240 110 C160 140 120 160 70 230 C40 280 20 300 0 310 Z" fill="var(--blue-blob)" opacity=".55"/>
    <path d="M0 560 C60 560 90 620 80 700 C70 790 150 800 220 830 C260 850 280 880 290 900 H0 Z" fill="var(--blue-blob)" opacity=".5"/>
    <path d="M636 0 V80 C580 70 520 40 500 0 Z" fill="var(--blue-blob)" opacity=".35"/>
  </svg>

  <div class="flyer-shapes" role="img" aria-label="Faint decorative particles scattered across the background">
    <svg viewBox="0 0 636 900" width="636" height="900">
      <circle cx="430" cy="28" r="40" fill="var(--blue-deep)" opacity=".35"/>
      <circle cx="150" cy="70" r="34" fill="var(--blue-deep)" opacity=".3"/>
      <circle cx="30" cy="420" r="38" fill="var(--blue-deep)" opacity=".25"/>
      <circle cx="230" cy="640" r="42" fill="var(--blue-deep)" opacity=".18"/>
      <circle cx="120" cy="760" r="48" fill="var(--navy)" opacity=".35"/>
    </svg>
  </div>

  <div class="brand">
    <span class="brand-mark"></span>
    <span class="brand-name">Clearway</span>
  </div>

  <header class="header">
    <h1 class="title">Coronavirus Covid-19</h1>
    <p class="subtitle">Information And Guidelines</p>
    <div class="rule"></div>
    <h2 class="kicker">THE EXIT STRATEGY</h2>
    <p class="quote">"Lorem ipsum dolor sit amet, consectetur adipiscing elit, sed do eiusmod tempor incididunt ut labore et dolore magna aliqua"</p>
  </header>

  <section class="guidelines">
    <div class="column left">
      <article class="guide">
        <div class="guide-icon"><svg width="24" height="24" viewBox="0 0 24 24" fill="none" stroke="var(--navy)" stroke-width="1.6"><path d="M7 20 V11 a2 2 0 0 1 4 0 V20 M13 20 V11 a2 2 0 0 1 4 0 V20"/><path d="M18 4 l1 2 M5 4 l-1 2"/></svg></div>
        <div><h3 class="guide-heading">Lorem Ipsum</h3><p class="guide-text">Mauris erat odio, porttitor nec ex vel, placerat finibus ante. Vivamus congue et massa sit amet vehicula. Aliquam mattis venenatis tortor vitae egestas.</p></div>
      </article>
      <article class="guide">
        <div class="guide-icon"><svg width="24" height="24" viewBox="0 0 24 24" fill="none" stroke="var(--navy)" stroke-width="1.6"><path d="M12 3 L19 6 V12 C19 16 16 19 12 21 C8 19 5 16 5 12 V6 Z"/><path d="M9 12 l2 2 4-4"/></svg></div>
        <div><h3 class="guide-heading">Lorem Ipsum</h3><p class="guide-text">Mauris erat odio, porttitor nec ex vel, placerat finibus ante. Vivamus congue et massa sit amet vehicula. Aliquam mattis venenatis tortor vitae egestas.</p></div>
      </article>
      <article class="guide">
        <div class="guide-icon"><svg width="24" height="24" viewBox="0 0 24 24" fill="none" stroke="var(--navy)" stroke-width="1.6"><rect x="6" y="8" width="12" height="8" rx="3"/><path d="M6 10 H3 M18 10 H21"/></svg></div>
        <div><h3 class="guide-heading">Lorem Ipsum</h3><p class="guide-text">Mauris erat odio, porttitor nec ex vel, placerat finibus ante. Vivamus congue et massa sit amet vehicula. Aliquam mattis venenatis tortor vitae egestas.</p></div>
      </article>
    </div>
    <div class="column right">
      <article class="guide">
        <div class="guide-icon"><svg width="24" height="24" viewBox="0 0 24 24" fill="none" stroke="var(--navy)" stroke-width="1.6"><path d="M4 11 L12 4 L20 11 V20 H4 Z"/><path d="M10 20 V14 H14 V20"/></svg></div>
        <div><h3 class="guide-heading">Lorem Ipsum</h3><p class="guide-text">Mauris erat odio, porttitor nec ex vel, placerat finibus ante. Vivamus congue et massa sit amet vehicula. Aliquam mattis venenatis tortor vitae egestas.</p></div>
      </article>
      <article class="guide">
        <div class="guide-icon"><svg width="24" height="24" viewBox="0 0 24 24" fill="none" stroke="var(--navy)" stroke-width="1.6"><path d="M9 3 H13 M10 3 V18 a2 2 0 0 0 2 0 V3"/><circle cx="18" cy="7" r="2.5"/></svg></div>
        <div><h3 class="guide-heading">Lorem Ipsum</h3><p class="guide-text">Mauris erat odio, porttitor nec ex vel, placerat finibus ante. Vivamus congue et massa sit amet vehicula. Aliquam mattis venenatis tortor vitae egestas.</p></div>
      </article>
      <article class="guide">
        <div class="guide-icon"><svg width="24" height="24" viewBox="0 0 24 24" fill="none" stroke="var(--navy)" stroke-width="1.6"><path d="M12 3 L19 6 V12 C19 16 16 19 12 21 C8 19 5 16 5 12 V6 Z"/><path d="M12 9 V15 M9 12 H15"/></svg></div>
        <div><h3 class="guide-heading">Lorem Ipsum</h3><p class="guide-text">Mauris erat odio, porttitor nec ex vel, placerat finibus ante. Vivamus congue et massa sit amet vehicula. Aliquam mattis venenatis tortor vitae egestas.</p></div>
      </article>
    </div>
  </section>

  <div class="photo" role="img" aria-label="Photo of hands being washed with soap"></div>

  <footer class="contact">
    <p class="contact-label">For information:</p>
    <p class="contact-line"><svg width="16" height="16" viewBox="0 0 24 24" fill="none" stroke="var(--white)" stroke-width="2"><path d="M5 3 H9 L11 8 L8 10 C9 13 11 15 14 16 L16 13 L21 15 V19 C21 20 20 21 19 21 C10 21 3 14 3 5 C3 4 4 3 5 3 Z"/></svg>55210 - 3908</p>
    <p class="contact-line"><svg width="16" height="16" viewBox="0 0 24 24" fill="none" stroke="var(--white)" stroke-width="2"><circle cx="12" cy="12" r="9"/><path d="M3 12 H21 M12 3 C8 8 8 16 12 21 C16 16 16 8 12 3"/></svg>www.clearwayhealth.co</p>
    <p class="social"><span class="social-dot"></span>@clearwayhealth</p>
  </footer>
</main>
</body>
</html>
```